"STYLE SNACKS" courses banner ads

Creation of 6 web banners for google display network and 1 image to be used on FaceBook.

Our website: http://www.qmvrk.org/
Our facebook: https://www.facebook.com/qmvrk/

The banners are meant to attract consumers to click and go to our landing page to find out more about our series of short courses training to be held in 4/5* hotels. The courses to be trained are Colour and Styling, Fabric Care and Leather Care.

Example of the short courses landing page: http://www.qmvrk.org/special-holiday-season-courses/

Target Market(s)

Females, 25-55 years old, interested in learning fashion styling, fabric care

Industry/Entity Type

Fashion

Font styles to use
Sans Serif

Colors
ec1f27
757575

Requirements
Must have
• Image used should have people and are happy/smiling.
• Some samples of pass banner ads images will be included: see the fabric care and open house samples
• Corporate colours are red, grey and black but addition of complementary colours will be great. Not necessary to use all the three corporate colours at the same time.
• Logos - to be provided (QmV.rk)
• TEXT:
• Style Snacks
• Short Courses held in hotels in June and July 2017
• Find out more!
Nice to have
• Asian person(s) in the image - please propose the stock image if necessary.
Should not have
• clip art
• fashion runway

```html
<!DOCTYPE html>
<html lang="en">
<head>
<meta charset="utf-8">
<title>Style Snacks – banner set</title>
<link href="https://fonts.googleapis.com/css2?family=Open+Sans:wght@800&family=PT+Sans:wght@400;700&display=swap" rel="stylesheet">
<style>
  :root {
    --backdrop: #433f40;
    --brand-red: #c5070c;
    --white: #ffffff;
    --ink: #222222;
    --photo-light: #e9b5c8;
    --photo-mid: #d9789c;
    --photo-deep: #c23f72;
    --cta-top: #3cb634;
    --cta-bottom: #0d7a12;
    --cta-edge: #0b3d0c;
  }
  html, body {
    margin: 0; padding: 0;
    width: 1200px; height: 1200px;
    overflow: hidden;
    background: var(--backdrop);
  }
  .canvas { position: relative; width: 1200px; height: 1200px; }

  .banner {
    position: absolute;
    display: flex;
    background: var(--white);
    box-shadow: 0 1px 3px rgba(0,0,0,.5);
    overflow: hidden;
  }
  .banner--tall { flex-direction: column; }

  .headline-panel {
    background: var(--brand-red);
    color: var(--white);
    display: flex;
    flex-direction: column;
    align-items: center;
    justify-content: center;
    text-align: center;
    box-sizing: border-box;
  }
  .title {
    font-family: "Open Sans", Verdana, sans-serif;
    font-weight: 800;
    line-height: .95;
    letter-spacing: .5px;
    margin: 0;
  }
  .subtitle {
    font-family: "PT Sans", Arial, sans-serif;
    font-weight: 700;
    line-height: 1.12;
    margin: 0;
  }

  .photo {
    background:
      radial-gradient(ellipse at 30% 65%, var(--photo-deep) 0%, transparent 45%),
      radial-gradient(ellipse at 75% 40%, var(--photo-mid) 0%, transparent 55%),
      linear-gradient(160deg, var(--photo-light), var(--photo-mid));
  }

  .footer-panel {
    flex: 1;
    display: flex;
    flex-direction: column;
    align-items: center;
    justify-content: center;
    background: var(--white);
  }

  .wordmark {
    font-family: "PT Sans", Arial, sans-serif;
    font-weight: 400;
    color: var(--ink);
    line-height: 1;
    white-space: nowrap;
  }

  .cta {
    position: relative;
    font-family: "PT Sans", Arial, sans-serif;
    font-weight: 700;
    color: var(--white);
    background: linear-gradient(var(--cta-top), var(--cta-bottom));
    border-bottom: 3px solid var(--cta-edge);
    border-radius: 3px;
    text-align: center;
    white-space: nowrap;
    box-sizing: border-box;
  }
  .cta::after {
    content: "";
    position: absolute;
    left: 50%; bottom: -6px;
    transform: translateX(-50%);
    border: 3px solid transparent;
    border-top-color: var(--white);
  }

  /* Skyscraper 160x600 */
  .banner--sky-wide { left: 267px; top: 258px; width: 130px; height: 481px; }
  .banner--sky-wide .headline-panel { height: 128px; padding-top: 6px; }
  .banner--sky-wide .title { font-size: 29px; }
  .banner--sky-wide .subtitle { font-size: 13px; margin-top: 10px; }
  .banner--sky-wide .photo { height: 260px; }
  .banner--sky-wide .wordmark { font-size: 28px; }
  .banner--sky-wide .cta { font-size: 14px; width: 105px; padding: 3px 0 2px; margin-top: 12px; }

  /* Skyscraper 120x600 */
  .banner--sky-narrow { left: 427px; top: 258px; width: 98px; height: 481px; }
  .banner--sky-narrow .headline-panel { height: 123px; }
  .banner--sky-narrow .title { font-size: 20px; }
  .banner--sky-narrow .subtitle { font-size: 12px; margin-top: 8px; }
  .banner--sky-narrow .photo { height: 263px; }
  .banner--sky-narrow .wordmark { font-size: 24px; }
  .banner--sky-narrow .cta { font-size: 11px; width: 85px; padding: 2px 0 1px; margin-top: 12px; }

  /* Standalone wordmark */
  .brand-lockup { position: absolute; left: 608px; top: 362px; width: 200px; display: flex; justify-content: center; }
  .brand-lockup .wordmark { font-size: 60px; color: #1f1d1e; }

  /* Medium rectangle 336x280 */
  .banner--rect { left: 573px; top: 514px; width: 270px; height: 226px; flex-direction: column; }
  .banner--rect .headline-panel { height: 64px; }
  .banner--rect .title { font-size: 34px; }
  .banner--rect .subtitle { font-size: 13px; margin-top: 1px; }
  .banner--rect .photo { height: 109px; }
  .banner--rect .footer-panel { flex-direction: row; justify-content: space-between; padding: 0 13px 0 26px; }
  .banner--rect .wordmark { font-size: 30px; }
  .banner--rect .cta { font-size: 14px; width: 105px; padding: 3px 0 2px; }

  /* Horizontal banners */
  .banner--wide .headline-panel { flex-direction: row; justify-content: space-evenly; }
  .banner--wide .title { text-align: center; }
  .banner--wide .subtitle { text-align: center; }

  .banner--468 { left: 270px; top: 782px; width: 258px; height: 41px; }
  .banner--468 .headline-panel { width: 109px; }
  .banner--468 .title { font-size: 13px; }
  .banner--468 .subtitle { font-size: 6px; }
  .banner--468 .photo { width: 93px; }
  .banner--468 .wordmark { font-size: 14px; }
  .banner--468 .cta { font-size: 6px; width: 46px; padding: 1px 0 0; border-bottom-width: 1px; margin-top: 3px; }
  .banner--468 .cta::after { border-width: 2px; bottom: -4px; }

  .banner--medium { left: 270px; top: 843px; width: 376px; height: 48px; }
  .banner--medium .headline-panel { width: 150px; }
  .banner--medium .title { font-size: 18px; }
  .banner--medium .subtitle { font-size: 8px; }
  .banner--medium .photo { width: 150px; }
  .banner--medium .wordmark { font-size: 17px; }
  .banner--medium .cta { font-size: 8px; width: 68px; padding: 1px 0 0; border-bottom-width: 2px; margin-top: 5px; }

  .banner--leader { left: 267px; top: 919px; width: 586px; height: 74px; }
  .banner--leader .headline-panel { width: 234px; }
  .banner--leader .title { font-size: 28px; }
  .banner--leader .subtitle { font-size: 12px; }
  .banner--leader .photo { width: 233px; }
  .banner--leader .wordmark { font-size: 24px; }
  .banner--leader .cta { font-size: 13px; width: 105px; padding: 2px 0 1px; margin-top: 8px; }
</style>
</head>
<body>
<main class="canvas">

  <section class="banner banner--tall banner--sky-wide">
    <div class="headline-panel">
      <h2 class="title">Style<br>Snacks</h2>
      <p class="subtitle">Short Courses held<br>in hotels in<br>June and July 2017</p>
    </div>
    <div class="photo" role="img" aria-label="Smiling woman in a pink lace dress beside spools of pink thread"></div>
    <div class="footer-panel">
      <div class="wordmark">QmV.rk</div>
      <div class="cta">Find out more!</div>
    </div>
  </section>

  <section class="banner banner--tall banner--sky-narrow">
    <div class="headline-panel">
      <h2 class="title">Style<br>Snacks</h2>
      <p class="subtitle">Short Courses<br>held in hotels<br>in June and<br>July 2017</p>
    </div>
    <div class="photo" role="img" aria-label="Smiling woman in a pink lace dress beside spools of pink thread"></div>
    <div class="footer-panel">
      <div class="wordmark">QmV.rk</div>
      <div class="cta">Find out more!</div>
    </div>
  </section>

  <div class="brand-lockup">
    <div class="wordmark">QmV.rk</div>
  </div>

  <section class="banner banner--rect">
    <div class="headline-panel">
      <h2 class="title">Style Snacks</h2>
      <p class="subtitle">Short Courses held in<br>hotels in June and July 2017</p>
    </div>
    <div class="photo" role="img" aria-label="Smiling woman beside pink thread spools and a tape measure"></div>
    <div class="footer-panel">
      <div class="wordmark">QmV.rk</div>
      <div class="cta">Find out more!</div>
    </div>
  </section>

  <section class="banner banner--wide banner--468">
    <div class="headline-panel">
      <h2 class="title">Style<br>Snacks</h2>
      <p class="subtitle">Short Courses<br>held in hotels<br>in June and<br>July 2017</p>
    </div>
    <div class="photo" role="img" aria-label="Smiling woman beside pink thread spools"></div>
    <div class="footer-panel">
      <div class="wordmark">QmV.rk</div>
      <div class="cta">Find out more!</div>
    </div>
  </section>

  <section class="banner banner--wide banner--medium">
    <div class="headline-panel">
      <h2 class="title">Style<br>Snacks</h2>
      <p class="subtitle">Short Courses<br>held in hotels<br>in June and<br>July 2017</p>
    </div>
    <div class="photo" role="img" aria-label="Smiling woman beside pink thread spools"></div>
    <div class="footer-panel">
      <div class="wordmark">QmV.rk</div>
      <div class="cta">Find out more!</div>
    </div>
  </section>

  <section class="banner banner--wide banner--leader">
    <div class="headline-panel">
      <h2 class="title">Style<br>Snacks</h2>
      <p class="subtitle">Short Courses<br>held in hotels<br>in June and<br>July 2017</p>
    </div>
    <div class="photo" role="img" aria-label="Smiling woman beside pink thread spools and a tape measure"></div>
    <div class="footer-panel">
      <div class="wordmark">QmV.rk</div>
      <div class="cta">Find out more!</div>
    </div>
  </section>

</main>
</body>
</html>
```